Company Business Card Design Project - Revamp the image of an old construction company.

We need a business card designed for a new company in Australia.

Type of business is Commercial Roofing & Painting.

Medium will be brushed black metal card that can/will be acid etched to a brushed steel silver, acid die cut and two printed colours of our choice which will be white and pantone orange.

We have hopes that the design will be simple, modern and represent with a quick glance what our company does.

Please read instructions carefully in must have box any questions please ask.

If you are interested in this job please look at other job that we have which is very similar with logo and design

Please have a look at the things that can be done with metals cards on google images for inspiration.

Target Market(s)

Business owners, commercial property development Men from 25-70 years of age.

Industry/Entity Type

Construction

Requirements
Must have
• Front of card:

Must use the company logo and name provided as attachment (see below norwick vale construction_black_background).

the words -Commercial Painting and Roofing- must be on front of card

details needed on front or back depending on your design

Name
position
email
mobile

all details can be on front with a cool design to be etched on the back of card or to keep front simple you can put all detail on back of card, I will leave the lay out to you.

Colours in logo are

Pantone 144 C Orange
Pantone 11-0601 White
Pantone 7539 C Gray
Pantone 426 C Black

However black will be the base of black metal card. Gray will be replaced with the etching in card revealing the silver. Orange and white will be printed on card.

Please have fun!!
Should not have
• Please don't clutter the card
No fonts smaller then 7 points

```html
<!DOCTYPE html>
<html lang="en">
<head>
<meta charset="utf-8">
<title>Norwick Vale – Business Card</title>
<link rel="stylesheet" href="https://fonts.googleapis.com/css2?family=Roboto:wght@300;400;700&display=swap">
<style>
  :root {
    --stage: #e9e6e2;
    --card-dark: #2f2f2f;
    --card-mid: #454545;
    --orange: #f47a20;
    --orange-deep: #e8601c;
    --silver: #b9b9b9;
    --silver-light: #dcdcdc;
    --ink: #262626;
    --text-soft: #d6d6d6;
  }
  * { box-sizing: border-box; margin: 0; padding: 0; }
  html, body { width: 1200px; height: 686px; overflow: hidden; }
  body {
    background: var(--stage);
    font-family: "Roboto", Arial, sans-serif;
    position: relative;
  }
  .card {
    position: absolute;
    top: 189px;
    width: 540px;
    height: 308px;
    border-radius: 6px;
    overflow: hidden;
    background:
      repeating-linear-gradient(90deg, rgba(255,255,255,0.025) 0 3px, rgba(0,0,0,0.04) 3px 7px),
      radial-gradient(ellipse at 45% 35%, var(--card-mid), var(--card-dark) 75%);
    box-shadow: 0 8px 24px rgba(0,0,0,0.25);
  }
  .card-front { left: 40px; }
  .card-back { left: 620px; }
  .card-shapes { position: absolute; inset: 0; }

  .brand {
    position: absolute;
    left: 48px;
    top: 128px;
    display: flex;
    align-items: center;
    gap: 10px;
  }
  .brand-mark {
    width: 14px; height: 14px;
    background: var(--silver);
  }
  .brand-name {
    color: var(--orange);
    font-weight: 700;
    font-size: 24px;
    letter-spacing: 1px;
  }
  .divider {
    position: absolute;
    left: 272px; top: 24px;
    width: 1px; height: 150px;
    background: linear-gradient(var(--silver-light), rgba(185,185,185,0.1));
  }
  .contact {
    position: absolute;
    left: 292px; top: 24px;
  }
  .contact-name {
    color: var(--orange);
    font-weight: 700;
    font-size: 22px;
  }
  .contact-position {
    color: var(--text-soft);
    font-size: 13px;
    font-weight: 300;
    margin-top: 6px;
  }
  .contact-list { list-style: none; margin-top: 14px; }
  .contact-list li {
    color: var(--text-soft);
    font-size: 14px;
    font-weight: 300;
    display: flex;
    align-items: center;
    gap: 8px;
    margin-bottom: 12px;
  }
  .contact-list svg { width: 13px; height: 13px; fill: var(--silver-light); }
  .tagline {
    position: absolute;
    right: 20px; top: 238px;
    text-align: right;
    color: var(--ink);
    font-weight: 700;
    font-size: 15px;
    letter-spacing: 1.5px;
    line-height: 22px;
  }

  .back-brand {
    position: absolute;
    left: 0; right: 0; top: 110px;
    display: flex;
    justify-content: center;
    align-items: center;
    gap: 14px;
  }
  .back-brand .brand-mark { width: 24px; height: 24px; }
  .back-brand .brand-name { font-size: 40px; letter-spacing: 2px; }
  .back-web {
    position: absolute;
    left: 0; right: 0; bottom: 34px;
    text-align: center;
    color: var(--ink);
    font-size: 15px;
    font-weight: 700;
    letter-spacing: 8px;
  }
</style>
</head>
<body>

<section class="card card-front" aria-label="Business card front">
  <svg class="card-shapes" viewBox="0 0 540 308" aria-hidden="true">
    <path d="M0 0 L135 0 C80 6 35 25 0 60 Z" fill="var(--orange)"/>
    <path d="M0 72 C40 30 95 10 170 4" fill="none" stroke="var(--silver)" stroke-width="4"/>
    <path d="M60 308 C220 300 380 230 540 130 L540 308 Z" fill="var(--orange-deep)"/>
    <path d="M30 300 C200 292 370 220 540 116" fill="none" stroke="var(--orange)" stroke-width="3"/>
    <path d="M0 238 C50 280 110 294 180 296" fill="none" stroke="var(--silver)" stroke-width="8"/>
    <path d="M0 262 C50 296 110 304 170 308 L0 308 Z" fill="var(--orange)"/>
  </svg>

  <div class="brand">
    <span class="brand-mark"></span>
    <span class="brand-name">NORWICK VALE</span>
  </div>

  <div class="divider"></div>

  <div class="contact">
    <p class="contact-name">Your Name</p>
    <p class="contact-position">Position</p>
    <ul class="contact-list">
      <li><svg viewBox="0 0 24 24"><path d="M6.6 10.8a15 15 0 0 0 6.6 6.6l2.2-2.2c.3-.3.7-.4 1-.2 1.1.4 2.3.6 3.6.6.6 0 1 .4 1 1V20c0 .6-.4 1-1 1C10.6 21 3 13.4 3 4c0-.6.4-1 1-1h3.5c.6 0 1 .4 1 1 0 1.3.2 2.5.6 3.6.1.3 0 .7-.2 1z"/></svg>985 210 4400</li>
      <li><svg viewBox="0 0 24 24"><path d="M2 5h20v14H2z M2 5l10 8 10-8" fill="none" stroke="var(--silver-light)" stroke-width="2"/></svg>info@norwickvale.com</li>
      <li><svg viewBox="0 0 24 24"><circle cx="12" cy="12" r="9" fill="none" stroke="var(--silver-light)" stroke-width="2"/><path d="M3 12h18M12 3c3 3 3 15 0 18M12 3c-3 3-3 15 0 18" fill="none" stroke="var(--silver-light)" stroke-width="1.5"/></svg>www.norwickvale.com</li>
    </ul>
  </div>

  <p class="tagline">Commercial<br>Painting and Roofing</p>
</section>

<section class="card card-back" aria-label="Business card back">
  <div class="back-brand">
    <span class="brand-mark"></span>
    <span class="brand-name">NORWICK VALE</span>
  </div>
  <p class="back-web">www.norwickvale.com</p>
</section>

</body>
</html>
```